Business Card Design Project

Hi,

We are a new modern sheet metal business and I require a business card for our sales reps.

The card should be double sided and standout in a crowd.

I have attached our logo and our website is www.plyform.com.au.

Please ask if you have any further questions
Updates

hi everyone, 

I'm wondering if we can try to lighten the cards mood.  Everyone is using black and I'm not sure how that would be accepted in real life.

Gordon

Reason: Still No receiving what I was hoping for.

Industry/Entity Type

Business

Requirements
Must have
• double sided

```html
<!DOCTYPE html>
<html lang="en">
<head>
<meta charset="utf-8">
<title>Plyform Sheetmetal – Business Card</title>
<link rel="stylesheet" href="https://fonts.googleapis.com/css2?family=Jost:wght@400;600&family=Tinos:wght@400;700&display=swap">
<style>
  :root {
    --navy: #2a3a8c;
    --navy-deep: #1f2c70;
    --steel: #b9bcc4;
    --steel-light: #e4e5e9;
    --paper: #ffffff;
    --ink: #2b2b33;
    --tagline: #4a4a52;
    --stage: #eceef1;
  }
  * { box-sizing: border-box; margin: 0; padding: 0; }
  html, body { width: 1200px; height: 900px; overflow: hidden; }
  body {
    background: var(--stage);
    position: relative;
    font-family: "Tinos", "Times New Roman", serif;
    color: var(--ink);
  }
  .card {
    position: absolute;
    left: 250px;
    width: 700px;
    height: 400px;
    background: linear-gradient(135deg, var(--paper) 45%, #f1f2f4 100%);
    box-shadow: 0 6px 18px rgba(0,0,0,.18);
    overflow: hidden;
  }
  .card-front { top: 40px; }
  .card-back { top: 460px; }
  .card-shapes { position: absolute; inset: 0; width: 700px; height: 400px; }

  .brand {
    position: absolute;
    display: flex;
    align-items: center;
    gap: 14px;
  }
  .brand-square { width: 24px; height: 24px; background: var(--navy); flex: none; }
  .brand-name {
    font-family: "Jost", "Helvetica", sans-serif;
    font-weight: 600;
    color: var(--navy);
    text-transform: uppercase;
    line-height: 1.02;
    white-space: nowrap;
  }
  .card-front .brand { left: 34px; top: 60px; }
  .card-front .brand-name { font-size: 44px; letter-spacing: 1px; }

  .tagline {
    position: absolute;
    font-family: "Jost", "Helvetica", sans-serif;
    color: var(--tagline);
    white-space: nowrap;
  }
  .tagline .bar {
    display: inline-block;
    width: 3px;
    height: 0.95em;
    background: var(--navy);
    margin: 0 7px;
    vertical-align: -2px;
  }
  .card-front .tagline { left: 30px; top: 218px; font-size: 17px; }

  .website { position: absolute; left: 425px; top: 40px; line-height: 1.1; }
  .website-label { font-size: 20px; color: var(--ink); }
  .website-url { font-size: 23px; font-weight: 700; color: var(--navy); letter-spacing: .3px; }

  .rep-slot {
    position: absolute;
    left: 380px;
    top: 122px;
    width: 298px;
    height: 62px;
    background: linear-gradient(180deg, #d9dade 0%, #c9cbd1 60%, #e6e7ea 100%);
    clip-path: polygon(6% 12%, 20% 4%, 40% 10%, 62% 2%, 84% 9%, 100% 3%, 100% 92%, 78% 100%, 55% 93%, 30% 100%, 10% 94%, 0% 100%, 2% 55%);
  }
  .rep-rule {
    position: absolute;
    left: 430px;
    top: 168px;
    width: 245px;
    height: 1px;
    background: var(--navy);
  }
  .rep-title {
    position: absolute;
    left: 430px;
    top: 172px;
    width: 245px;
    text-align: right;
    font-size: 12px;
    font-weight: 700;
    font-variant: small-caps;
    letter-spacing: 1.5px;
    color: var(--navy);
  }

  .contact-line {
    position: absolute;
    left: 32px;
    top: 270px;
    font-size: 19px;
    color: var(--ink);
  }
  .contact-line strong { color: var(--navy); font-weight: 700; }
  .contact-line .sep { margin: 0 8px; color: var(--ink); }

  .address { position: absolute; left: 32px; top: 308px; line-height: 1.1; }
  .address-label { font-size: 19px; }
  .address-line { font-size: 15px; font-weight: 700; color: var(--navy); }

  .card-back .brand {
    left: 0; right: 0; top: 100px;
    justify-content: center;
  }
  .card-back .brand-name { font-size: 56px; letter-spacing: 1.5px; }
  .card-back .tagline {
    left: 0; right: 0; top: 240px;
    text-align: center;
    font-size: 19px;
  }
</style>
</head>
<body>

  <section class="card card-front" aria-label="Business card, front">
    <svg class="card-shapes" viewBox="0 0 700 400" aria-hidden="true">
      <rect x="0" y="0" width="700" height="22" fill="var(--steel-light)"/>
      <rect x="0" y="22" width="700" height="3" fill="var(--steel)"/>
      <polygon points="0,388 420,384 700,336 700,400 0,400" fill="var(--navy)"/>
      <polygon points="0,382 420,378 700,328 700,336 420,384 0,388" fill="var(--steel)"/>
      <line x1="30" y1="250" x2="380" y2="250" stroke="var(--steel-light)" stroke-width="2"/>
    </svg>

    <div class="brand">
      <span class="brand-square"></span>
      <span class="brand-name">Plyform<br>Sheetmetal</span>
    </div>
    <p class="tagline">Flashings<span class="bar"></span>Gutter<span class="bar"></span>Rainwater Goods</p>

    <div class="website">
      <p class="website-label">Website:</p>
      <p class="website-url">www.plyform.com.au</p>
    </div>

    <div class="rep-slot" role="img" aria-label="Torn paper strip revealing space for the sales representative's name"></div>
    <div class="rep-rule"></div>
    <p class="rep-title">Sales Representative</p>

    <p class="contact-line">Phone: <strong>3555 0142</strong><span class="sep">|</span>Fax: <strong>3555 0187</strong></p>

    <div class="address">
      <p class="address-label">Address:</p>
      <p class="address-line">28 Quartz Road Ridgeview Q 4300</p>
      <p class="address-line">P.O. Box 590 Ridgeview Q 4300</p>
    </div>
  </section>

  <section class="card card-back" aria-label="Business card, back">
    <svg class="card-shapes" viewBox="0 0 700 400" aria-hidden="true">
      <polygon points="560,0 700,0 700,60" fill="var(--steel-light)"/>
      <polygon points="0,0 40,0 40,400 0,400" fill="var(--navy)"/>
      <polygon points="40,0 48,0 48,400 40,400" fill="var(--steel)"/>
      <polygon points="0,330 700,372 700,400 0,400" fill="var(--navy)"/>
      <polygon points="0,322 700,364 700,372 0,330" fill="var(--steel)"/>
    </svg>

    <div class="brand">
      <span class="brand-square"></span>
      <span class="brand-name">Plyform<br>Sheetmetal</span>
    </div>
    <p class="tagline">Flashings<span class="bar"></span>Gutter<span class="bar"></span>Rainwater Goods</p>
  </section>

</body>
</html>
```